Integrative Medical Practice Website Redo

I am needing to have our current website redesigned to make it a responsive website to work on smartphones.
Current website
www.brightoakfm.com
Here are several examples of what I am looking for
https://www.corvanhealth.com/
I am wanting a popup for a newsletter signup
Looking for a very professional, clean, simple, minimalist, bold well designed website
Colors would ideally be greens and blues, cool tones, muted colors, or graytones like:
https://journeybright.org/
Several other clean design examples
http://7harborsrenton.com/
http://www.belvomedical.com/
http://sunpathyouth.com/
http://yourcellduke.com/
I would like the top navigation bar to be able to slide down while browsing site
We are also needing to add several features that are not on our current website:
Questionnaire buttons
Are you toxic questionnaire?
Take our hormone quiz to find out if hormones are affecting your health.
online scheduling option for:
nutrition counselling
testing like body composition, basal metabolic rate, CIMT, breast thermography, VO2 Max testing, Vita Trace
Therapies like whole body vibration, infrared sauna, Exercise with oxygen, hyperbaric oxygen, spinal decompression
Need to have separate page for different services and split up services into:
Consults/Office Visits, Testing, Therapies, Procedures
Need to have a button link to patient portal
Needs to have online store
Need to add navigation button "Start Here"
Need a spot for a video on practice summary
Newsletter signup to collect emails
Testimonials from linkpage
Blog that posts can be shared with social media
Password protected patient access that can integrate into crate.net ideally
Modules for programs online classes/videos
I have attached stock images that you can use, but feel free to find others to use.
I have also attached a copy of our current brochure that shows an overview of the practice
Target Market(s)
Health conscious people of all ages looking for a family medicine doctor
Industry/Entity Type
Alternative Medicine
Coding
Coded - Design and coding required
Number of Pages Required
5+ page
Look and feel

```html
<!DOCTYPE html>
<html lang="en">
<head>
<meta charset="utf-8">
<title>Bright Oak Family Medicine</title>
<link href="https://fonts.googleapis.com/css2?family=Cinzel:wght@400;700&family=Lato:wght@400;700&display=swap" rel="stylesheet">
<style>
:root{
  --blue:#3a9fd8;
  --teal:#3aa3c9;
  --green:#7db83a;
  --olive:#8a9a2c;
  --navy:#1d2c3a;
  --text:#555;
}
*{box-sizing:border-box;margin:0;padding:0}
html,body{width:1200px;height:4534px;overflow:hidden}
body{font-family:"Lato",Arial,sans-serif;color:var(--text);background:#fff;font-size:14px}
section,header,footer,nav{position:relative;width:1200px}
.heading{font-family:"Cinzel",Georgia,serif;color:var(--teal);text-align:center;font-weight:400;letter-spacing:1px}
.divider{position:absolute;left:540px;width:120px;height:10px}

/* top bar */
.topbar{height:28px;background:#f1f1f1;font-size:12px;color:#666}
.topbar .contact{position:absolute;left:90px;top:7px;display:flex;gap:30px}
.topbar .right{position:absolute;right:90px;top:7px;display:flex;gap:14px;align-items:center}
.topbar .soc{width:12px;height:12px;border-radius:2px;background:#9aa}

/* header */
.masthead{height:87px;background:#fff}
.brand{position:absolute;left:90px;top:20px;display:flex;align-items:center;gap:10px}
.brand .mark{width:34px;height:34px;border-radius:50%;background:var(--teal)}
.brand .name{font-weight:700;font-size:24px;color:var(--teal);line-height:1.05}
.btn-nutrition{position:absolute;left:604px;top:23px;width:196px;height:42px;background:var(--green);color:#fff;font-size:14px;display:flex;align-items:center;justify-content:center;gap:10px}
.header-link{position:absolute;top:32px;font-size:14px;color:#666;display:flex;align-items:center;gap:8px}

/* nav */
.mainnav{height:42px;background:var(--blue)}
.mainnav ul{list-style:none;display:flex;justify-content:space-between;position:absolute;left:100px;right:100px;top:12px}
.mainnav li{color:#fff;font-size:14px;font-weight:700}

/* hero */
.hero{height:531px;background:linear-gradient(180deg,#d8e6dc 0%,#c9d7c2 40%,#e6ddd2 100%)}
.hero .photo{position:absolute;inset:0;background:radial-gradient(ellipse at 55% 55%,#e8c7a8 0%,#d9b796 30%,rgba(220,225,215,0) 70%)}
.hero-banner{position:absolute;left:356px;top:371px;width:490px;height:55px;background:var(--green);color:#fff;font-size:24px;display:flex;align-items:center;justify-content:center}
.btn-start{position:absolute;left:540px;top:446px;width:122px;height:31px;background:var(--blue);color:#fff;font-size:12px;font-weight:700;letter-spacing:1px;display:flex;align-items:center;justify-content:center}

/* intro */
.intro{height:414px;background:linear-gradient(180deg,#fff 0%,#f5f6f5 100%)}
.intro h1{position:absolute;top:42px;left:0;width:1200px;font-size:30px;line-height:38px}
.intro p{position:absolute;top:206px;left:120px;width:960px;text-align:center;font-size:13.5px;line-height:19px;color:#666}
.btn-read{position:absolute;left:545px;top:337px;width:110px;height:30px;border:1px solid #888;font-size:13px;color:#444;display:flex;align-items:center;justify-content:center;background:#fff}

/* video */
.video{height:664px;background:linear-gradient(90deg,#3a4a22 0%,#4d5b2a 40%,#6d6a48 75%,#8f8a70 100%)}
.player{position:absolute;left:100px;top:51px;width:655px;height:502px;background:#111}
.player .title{position:absolute;left:10px;top:6px;color:#fff;font-size:12px}
.player .frame{position:absolute;left:0;top:22px;width:655px;height:455px;background:linear-gradient(135deg,#c98d6e,#e7b89b 50%,#b57a5c)}
.player .play{position:absolute;left:297px;top:219px;width:60px;height:60px;border-radius:50%;background:rgba(0,0,0,.45);border:2px solid #fff}
.player .bar{position:absolute;left:0;bottom:0;width:655px;height:25px;background:#222}
.player .progress{position:absolute;left:10px;top:10px;width:635px;height:3px;background:#555}
.player .progress i{display:block;width:410px;height:3px;background:#ccc}
.video h2{position:absolute;left:815px;top:312px;font-family:"Cinzel",serif;font-weight:400;font-size:26px;color:#fff;letter-spacing:1px}

/* services */
.services{height:801px;background:#fff}
.services h2{position:absolute;top:70px;width:1200px;font-size:26px}
.service-grid{position:absolute;left:105px;top:190px;width:990px;display:grid;grid-template-columns:repeat(4,1fr);row-gap:62px}
.service{text-align:center;height:120px}
.service svg{width:70px;height:70px;display:block;margin:0 auto 14px}
.service span{display:block;color:var(--teal);font-size:14px;line-height:18px}

/* formula */
.formula{height:423px;background:linear-gradient(90deg,#5cb3e4,#74c0e9 50%,#5cb3e4)}
.formula h2{position:absolute;top:72px;width:1200px;font-family:"Cinzel",serif;color:#1d3550;font-size:26px;font-weight:700;text-align:center}
.habits{position:absolute;left:115px;top:176px;width:970px;display:flex;justify-content:space-between}
.habit{width:180px;text-align:center;color:#1d3550;font-size:15px}
.habit .ring{width:100px;height:100px;margin:0 auto 20px;border-radius:50%;border:3px solid var(--olive);display:flex;align-items:center;justify-content:center}
.habit .ring i{width:76px;height:76px;border-radius:50%;background:var(--olive);display:flex;align-items:center;justify-content:center}

/* blog */
.blog{height:724px;background:#fff}
.blog h2{position:absolute;top:46px;width:1200px;font-size:26px}
.feature{position:absolute;left:90px;top:150px;width:500px;height:529px}
.feature .panel{position:absolute;left:0;top:0;width:257px;height:529px;background:#6f8a4a;color:#fff;padding:40px 36px}
.feature .panel .date{color:#b9e47a;font-size:19px;line-height:22px}
.feature .panel p{font-size:13px;line-height:19px;margin-top:14px}
.feature .panel .by{color:#b9e47a;font-size:12px;margin-top:18px}
.feature .arrows{position:absolute;left:36px;top:462px;display:flex;gap:8px}
.feature .arrows i{width:20px;height:20px;border-radius:50%;background:var(--blue)}
.feature .shot{position:absolute;left:257px;top:0;width:243px;height:529px;background:linear-gradient(180deg,#c9a274,#9e7448 60%,#d4c3a6)}
.posts{position:absolute;left:620px;top:150px;width:497px}
.post{position:relative;height:167px}
.post .thumb{position:absolute;left:0;top:0;width:157px;height:157px}
.post .body{position:absolute;left:185px;top:0;width:312px}
.post h3{font-size:15px;color:#333;font-weight:700}
.post h3 span{font-weight:400}
.post p{font-size:13px;line-height:19px;margin-top:12px;color:#666}
.post .by{font-size:11px;color:var(--teal);margin-top:8px}

/* testimonials */
.testimonials{height:438px;background:linear-gradient(180deg,#f3f4f4,#eef0f0)}
.testimonials h2{position:absolute;top:68px;width:1200px;font-size:28px}
.testimonials .sub{position:absolute;top:108px;width:1200px;text-align:center;font-size:24px;color:#555}
.avatar{position:absolute;left:557px;top:166px;width:86px;height:86px;border-radius:50%;background:#c9a58c;border:3px solid #fff}
.testimonials .who{position:absolute;top:274px;width:1200px;text-align:center;color:var(--teal);font-size:15px;font-weight:700}
.testimonials .place{position:absolute;top:296px;width:1200px;text-align:center;font-size:12px;color:#777}
.testimonials .quote{position:absolute;top:326px;left:230px;width:740px;text-align:center;font-size:13.5px;line-height:19px;color:#555}
.tarrow{position:absolute;top:200px;width:20px;height:40px}

/* footer */
.site-footer{height:318px;background:var(--navy);color:#cfd8df;font-size:13px}
.site-footer h4{color:#fff;font-size:15px;font-weight:700;margin-bottom:16px;display:flex;gap:10px;align-items:center}
.fcol{position:absolute;top:40px}
.hours{list-style:none}
.hours li{display:flex;height:21px;white-space:nowrap}
.hours li b{font-weight:400;width:90px}
.hours li em{font-style:normal;width:40px;color:#778}
.addr p{display:flex;gap:10px;align-items:flex-start;margin-bottom:8px;line-height:18px}
.dot{width:12px;height:12px;border-radius:50%;background:var(--green);flex:none;margin-top:3px}
.quiz{margin-top:22px}
.quiz p{color:#fff;font-weight:700;display:flex;gap:10px;margin-bottom:10px;line-height:18px}
.likebox{width:260px;height:130px;background:#fff;border:1px solid #ccc}
.likebox .cover{height:60px;background:linear-gradient(90deg,#6e8a4a,#a7b987)}
.likebox .name{color:#334;font-size:12px;font-weight:700;padding:6px 8px}
.likebox .faces{display:flex;gap:4px;padding:0 8px}
.likebox .faces i{width:22px;height:22px;background:#c8ccd2}
.bottombar{position:absolute;left:0;top:4470px;width:1200px;height:64px;background:var(--blue);color:#fff;font-size:12px;display:flex;align-items:center;justify-content:center}
</style>
</head>
<body>

<div class="topbar">
  <div class="contact"><span>&#9742; Phone: (555) 210-4471</span><span>&#9993; Email: info@brightoakfm.com</span></div>
  <div class="right"><span>Login</span><i class="soc"></i><i class="soc"></i><i class="soc"></i><i class="soc"></i><i class="soc"></i></div>
</div>

<header class="masthead">
  <div class="brand"><span class="mark"></span><span class="name">Bright Oak<br>Family Medicine</span></div>
  <div class="btn-nutrition">Nutrition Counselling <svg width="10" height="8" viewBox="0 0 10 8"><path d="M0 0h10L5 8z" fill="#fff"/></svg></div>
  <div class="header-link" style="left:830px"><svg width="20" height="16" viewBox="0 0 20 16"><path d="M1 1h3l2 10h11l2-7H5" fill="none" stroke="#777" stroke-width="1.5"/><circle cx="8" cy="14" r="1.5" fill="#777"/><circle cx="15" cy="14" r="1.5" fill="#777"/></svg>Online Store</div>
  <div class="header-link" style="left:1012px"><svg width="16" height="16" viewBox="0 0 16 16"><rect x="1" y="2" width="14" height="12" fill="none" stroke="#777" stroke-width="1.5"/></svg>Patient Portal</div>
</header>

<nav class="mainnav">
  <ul><li>Home</li><li>About us</li><li>Services</li><li>Resources</li><li>FAQ</li><li>Current Patients</li><li>New Patients</li><li>OakCare Membership</li><li>Testimonials</li><li>Blog</li><li>Contact</li></ul>
</nav>

<section class="hero">
  <div class="photo" role="img" aria-label="Smiling family of four outdoors"></div>
  <div class="hero-banner">Helping you get well, Stay well, and live well</div>
  <div class="btn-start">START HERE</div>
</section>

<section class="intro">
  <h1 class="heading">Restoring your health naturally<br>with nutrition, manipulation, acupuncture,<br>and integrative medicine</h1>
  <p>Welcome to our website. As an integrative medical practice, we provide innovative, quality family health care by uniquely combining both conventional and alternative medicine. Our aim is to treat the whole patient not just the symptoms. This "best of both worlds" approach provides patients with options in the management of their concerns while addressing the underlying cause of their illness. And as a primary care practice, we offer treatment for both acute and chronic conditions while emphasizing prevention, education and optimal health.</p>
  <div class="btn-read">Read more</div>
</section>

<section class="video">
  <div class="player">
    <div class="title">Acupuncture treatment for knee and ankle joint pain</div>
    <div class="frame" role="img" aria-label="Video still of an acupuncture treatment"></div>
    <div class="play"><svg width="56" height="56" viewBox="0 0 56 56"><path d="M22 17l16 11-16 11z" fill="#fff"/></svg></div>
    <div class="bar"><div class="progress"><i></i></div></div>
  </div>
  <h2>Practice Summary</h2>
</section>

<section class="services">
  <h2 class="heading">Our Services</h2>
  <div class="service-grid">
    <div class="service"><svg viewBox="0 0 70 70" fill="none" stroke="#8a9a2c" stroke-width="2.5"><path d="M12 30h46c0 14-10 24-23 24S12 44 12 30z"/><path d="M40 30l14-20"/><path d="M26 56h18"/></svg><span>Integrative Family Medicine</span></div>
    <div class="service"><svg viewBox="0 0 70 70" fill="none" stroke="#8a9a2c" stroke-width="2.5"><path d="M35 58L12 34a12 12 0 0 1 23-16 12 12 0 0 1 23 16z"/><path d="M14 36h12l4-8 6 14 4-6h16"/></svg><span>Functional Medicine</span></div>
    <div class="service"><svg viewBox="0 0 70 70" fill="none" stroke="#8a9a2c" stroke-width="2.5"><path d="M20 58l28-34-8-6z"/><path d="M46 20l8-10M48 24l12-4"/></svg><span>Nutrition</span></div>
    <div class="service"><svg viewBox="0 0 70 70" fill="none" stroke="#8a9a2c" stroke-width="2.5"><rect x="14" y="14" width="42" height="42" rx="6"/><path d="M24 28a14 10 0 0 1 22 0z"/></svg><span>Weight Loss</span></div>
    <div class="service"><svg viewBox="0 0 70 70" fill="none" stroke="#8a9a2c" stroke-width="2.5"><circle cx="35" cy="16" r="7"/><path d="M22 58V30h26v28M22 40h26"/></svg><span>Osteopathic Manipulation</span></div>
    <div class="service"><svg viewBox="0 0 70 70" fill="none" stroke="#8a9a2c" stroke-width="2.5"><path d="M14 56h42M22 56V30M35 56V22M48 56V34"/><path d="M18 22l8 8M31 14l8 8M44 26l8 8"/></svg><span>Acupuncture</span></div>
    <div class="service"><svg viewBox="0 0 70 70" fill="none" stroke="#8a9a2c" stroke-width="2.5"><path d="M16 54l26-26 8 8-26 26z"/><path d="M46 24l10-10M52 12l6 6M12 58l4-4"/></svg><span>Prolotherapy 7 ultrasound guided<br>PRP injections</span></div>
    <div class="service"><svg viewBox="0 0 70 70" fill="none" stroke="#8a9a2c" stroke-width="2.5"><rect x="20" y="20" width="30" height="38" rx="4"/><rect x="24" y="12" width="22" height="8"/><path d="M35 32v14M28 39h14"/></svg><span>Bio- indentical hormone<br>replacement</span></div>
    <div class="service"><svg viewBox="0 0 70 70" fill="none" stroke="#8a9a2c" stroke-width="2.5"><path d="M35 10l22 12v26L35 60 13 48V22z"/><path d="M35 22l11 6v14l-11 6-11-6V28z"/></svg><span>Labs</span></div>
    <div class="service"><svg viewBox="0 0 70 70" fill="none" stroke="#8a9a2c" stroke-width="2.5"><path d="M26 12h18M30 12v40a5 5 0 0 0 10 0V12"/><path d="M30 36h10"/></svg><span>Allergy testing treatment</span></div>
    <div class="service"><svg viewBox="0 0 70 70" fill="none" stroke="#8a9a2c" stroke-width="2.5"><path d="M14 56l30-30M40 16l14 14M44 12l14 14M18 48l4 4"/></svg><span>Other testing &amp; therapies</span></div>
    <div class="service"><svg viewBox="0 0 70 70" fill="none" stroke="#8a9a2c" stroke-width="2.5"><rect x="12" y="22" width="46" height="34" rx="4"/><path d="M26 22v-8h18v8M35 30v18M26 39h18"/></svg><span>View All Services</span></div>
  </div>
</section>

<section class="formula">
  <h2>Formula for Good Health</h2>
  <div class="habits">
    <div class="habit"><div class="ring"><i><svg width="40" height="40" viewBox="0 0 40 40" fill="none" stroke="#fff" stroke-width="2.5"><circle cx="20" cy="20" r="15"/><path d="M9 31L31 9"/></svg></i></div>NO SMOKING</div>
    <div class="habit"><div class="ring"><i><svg width="40" height="40" viewBox="0 0 40 40" fill="none" stroke="#fff" stroke-width="2.5"><path d="M6 20h28a14 12 0 0 1-28 0zM14 32h12"/></svg></i></div>HEALTHY EATING</div>
    <div class="habit"><div class="ring"><i><svg width="40" height="40" viewBox="0 0 40 40" fill="none" stroke="#fff" stroke-width="2.5"><circle cx="20" cy="9" r="4"/><path d="M8 16h24M20 16v10l-6 10M20 26l6 10"/></svg></i></div>HEALTHY WEIGHT</div>
    <div class="habit"><div class="ring"><i><svg width="40" height="40" viewBox="0 0 40 40" fill="none" stroke="#fff" stroke-width="2.5"><circle cx="10" cy="28" r="6"/><circle cx="30" cy="28" r="6"/><path d="M10 28l8-12h8l4 12M18 16l4 12"/></svg></i></div>DAILY EXERCISE</div>
    <div class="habit"><div class="ring"><i><svg width="40" height="40" viewBox="0 0 40 40" fill="none" stroke="#fff" stroke-width="2.5"><path d="M4 30h32M4 30V14M36 30v-8H16v8M8 22h6"/></svg></i></div>ADEQUATE SLEEP</div>
  </div>
</section>

<section class="blog">
  <h2 class="heading">Latest Blog</h2>
  <svg class="divider" style="top:84px" viewBox="0 0 120 10"><path d="M0 5h50M70 5h50" stroke="#b9c3a0"/><circle cx="60" cy="5" r="3" fill="#8a9a2c"/></svg>
  <div class="feature">
    <div class="panel">
      <div class="date">22 December<br>Sauna Bathing</div>
      <p>Here is a new study that just came out that studied 2,315 Finnish men that were using a sauna over 20 years. Using a sauna 2-3 times per week lowered dementia risk by 22%, and Alzheimer's to 20% whereas 4-7x per week lowered dementia risk by 66% &amp; Alzheimer's risk by 65% after adjusting for diet/lifestyle.</p>
      <div class="by">By Admin</div>
    </div>
    <div class="arrows"><i></i><i></i></div>
    <div class="shot" role="img" aria-label="Wooden sauna interior"></div>
  </div>
  <div class="posts">
    <div class="post">
      <div class="thumb" role="img" aria-label="Sauna room" style="background:linear-gradient(135deg,#c89060,#8d5a30)"></div>
      <div class="body"><h3>22 December : <span>Sauna Bathing</span></h3><p>Here is a study that just came out that studied 2,315 Finnish men that were using a sauna over 20 years.</p><div class="by">By Admin</div></div>
    </div>
    <div class="post">
      <div class="thumb" role="img" aria-label="Holiday gift promotion" style="background:linear-gradient(135deg,#c8262c,#5a8a3a)"></div>
      <div class="body"><h3>09 December : <span>Trying to find the perfect Christmas present.</span></h3><p>Right now GeneLine is offering $50 dollars off, making it now $149 until January 9, 2017. With Kin Finder and updated.</p><div class="by">By Admin</div></div>
    </div>
    <div class="post">
      <div class="thumb" role="img" aria-label="Snack bar packaging" style="background:linear-gradient(135deg,#e8d9b8,#9cb85a)"></div>
      <div class="body"><h3>26 November : <span>Food as Medicine</span></h3><p>Do you have a favorite protein snack bar? My favorite up till now has been Prairie Pantry's Dark Chocolate Almond.</p><div class="by">By Admin</div></div>
    </div>
  </div>
</section>

<section class="testimonials">
  <h2 class="heading">Testimonials</h2>
  <div class="sub">What our clients say about us</div>
  <svg class="tarrow" style="left:92px" viewBox="0 0 20 40"><path d="M18 2L2 20l16 18" fill="none" stroke="#999" stroke-width="2"/></svg>
  <svg class="tarrow" style="left:1088px" viewBox="0 0 20 40"><path d="M2 2l16 18L2 38" fill="none" stroke="#999" stroke-width="2"/></svg>
  <div class="avatar" role="img" aria-label="Client portrait"></div>
  <div class="who">Marla Quinn Dawson</div>
  <div class="place">Fairhaven, Texas</div>
  <div class="quote">Dr. Marsh has a caring personality and a fresh, more natural and wholistic perspective on health. He takes his time with appointments and concerns and doesn't rush. He's truly an asset to our healthcare team.</div>
</section>

<footer class="site-footer">
  <div class="fcol" style="left:106px">
    <h4><span class="dot" style="margin:0"></span>Clinic Timing</h4>
    <ul class="hours">
      <li><b>Monday</b><em>—</em>8 AM to 6 PM</li>
      <li><b>Wednesday</b><em>—</em>8 AM to 6 PM</li>
      <li><b>Friday</b><em>—</em>8 AM to 1 PM</li>
      <li><b>Tuesday</b><em>—</em>8 AM to 6 PM</li>
      <li><b>Thursday</b><em>—</em>8 AM to 6 PM</li>
      <li>Saturday &amp; Sunday off.</li>
    </ul>
    <p style="display:flex;gap:10px;margin-top:16px"><span class="dot"></span>The office is closed from 12-1 for lunch</p>
  </div>
  <div class="fcol addr" style="left:459px">
    <h4>Address</h4>
    <p><span class="dot"></span>418 Linden Court, Fairhaven,<br>TX 70412</p>
    <p><span class="dot"></span>(555) 210-4471</p>
    <p><span class="dot"></span>(555) 210-4486</p>
    <p><span class="dot"></span>info@brightoakfm.com</p>
    <div class="quiz">
      <p><span class="dot"></span>Are you toxic questionnaire?</p>
      <p><span class="dot"></span>Take our hormone quiz to find out if<br>hormones are affecting your health.</p>
    </div>
  </div>
  <div class="fcol" style="left:809px">
    <h4>Like us on linkpage</h4>
    <div class="likebox">
      <div class="cover" role="img" aria-label="Practice page cover image"></div>
      <div class="name">Bright Oak Family Medicine</div>
      <div class="faces"><i></i><i></i><i></i><i></i><i></i><i></i><i></i><i></i></div>
    </div>
  </div>
</footer>

<div class="bottombar">Copyright© brightoakfm 2017</div>

</body>
</html>
```